Web Design for an Innovative Life Science Marketplace

IMPORTANT:
The software is called CS-Cart. It has capabilities and limitations with design features in the software. There is a certain framework that needs to be followed. It is PHP and Linux. It may require add-ons for your design, so please be specific with what is required. It’s preferred the designer has CS-Cart knowledge/experience.

Key Requirements
1. I’d like the design to include an implemented/recommended CS-Cart theme that is consistent with our branding (see the marketing collateral and logo).
2. I then need the additional design changes to that theme to create the below web pages.
3. All designs should be consistent with our branding. All pictures should either be computer generated (clip art-like) or pictures of happy patients. What is a happy patient? Close up photo of someone healthy, happy, and experiencing/enjoying life. Not someone in a hospital or getting care. Please see examples already on the site.

Please see the attached Web Design details in the word document. That document is important to complete the design.

```html
<!DOCTYPE html>
<html lang="en">
<head>
<meta charset="utf-8">
<title>Veldora – White Paper</title>
<link href="https://fonts.googleapis.com/css2?family=Roboto:wght@400;500;700&family=Roboto+Condensed:wght@400;700&display=swap" rel="stylesheet">
<style>
:root{
  --teal:#219b8e;
  --green:#8dc63f;
  --ink:#555;
  --body:#8a8a8a;
  --dark:#2c2c2c;
  --white:#fff;
  --line:#e6e6e6;
}
*{box-sizing:border-box;margin:0;padding:0}
html,body{width:860px;height:1200px;overflow:hidden;background:var(--white)}
body{position:relative;font-family:'Roboto',sans-serif;color:var(--ink)}
.abs{position:absolute}
.topbar{top:0;left:0;width:860px;height:21px;border-bottom:1px solid var(--line);font-size:7px;color:#555}
.topbar .item{position:absolute;top:6px;display:flex;align-items:center;gap:5px;text-transform:uppercase}
.topbar .ico{width:8px;height:8px;background:var(--teal);border-radius:1px}
.btn-sm{position:absolute;top:1px;height:18px;border-radius:9px;color:var(--white);font-size:7px;font-weight:700;display:flex;align-items:center;justify-content:center}
.header{top:21px;left:0;width:860px;height:55px}
.brand{position:absolute;left:116px;top:18px;display:flex;align-items:center;gap:6px}
.brand .mark{width:22px;height:22px;border-radius:50%;border:2px solid var(--teal)}
.brand .name{font-family:'Roboto Condensed',sans-serif;font-weight:700;font-size:17px;color:var(--green);letter-spacing:.5px}
.cart{position:absolute;left:455px;top:11px;display:flex;gap:6px}
.cart .box{width:36px;height:31px;background:var(--green);display:flex;align-items:center;justify-content:center}
.cart .t1{font-family:'Roboto Condensed',sans-serif;font-size:11px;color:#555;margin-top:2px}
.cart .t2{font-size:7px;color:#666;display:flex;align-items:center;gap:2px}
.cart .t2 b{color:var(--green);font-size:14px}
.search{position:absolute;left:603px;top:14px;width:141px;height:25px;border-radius:13px;border:1px solid #eee;font-size:7px;color:#aaa;padding:9px 12px}
.search .go{position:absolute;right:5px;top:4px;width:16px;height:16px;border-radius:50%;background:var(--green)}
.nav{top:76px;left:0;width:860px;height:28px;background:var(--teal);display:flex;padding-left:100px}
.nav a{color:var(--white);font-size:8px;font-weight:500;text-decoration:none;padding:0 17px;line-height:28px;border-right:1px solid rgba(255,255,255,.15)}
.hero{top:104px;left:0;width:860px;height:167px;background:linear-gradient(90deg,#c9a98c 0%,#d9b9a0 40%,#b57d63 70%,#8a4e3f 100%)}
.title{top:308px;left:0;width:860px;text-align:center;font-family:'Roboto Condensed',sans-serif;font-weight:700;color:#555;font-size:27px}
.title .cap{color:var(--green);font-size:64px;line-height:50px}
.title .rule{display:inline-block;width:56px;height:1px;background:#555;vertical-align:middle;margin:0 3px}
.title .rule.short{width:18px}
.intro{top:380px;left:115px;width:630px;text-align:center;font-size:8px;line-height:13.5px;color:var(--body)}
.col{top:470px;width:292px}
.col h3{font-family:'Roboto Condensed',sans-serif;font-weight:700;font-size:17px;color:#555;margin-bottom:10px}
.col p{font-size:8px;line-height:13.5px;color:var(--body);margin-bottom:13px}
.btn{display:inline-flex;align-items:center;justify-content:center;width:83px;height:27px;border-radius:14px;background:var(--teal);color:var(--white);font-size:9px;font-family:'Roboto Condensed',sans-serif;font-weight:700;margin-top:3px}
.divider{left:430px;top:455px;width:1px;height:207px;background:var(--line)}
.contact{top:709px;left:0;width:860px;height:105px;background:linear-gradient(90deg,#8dc63f,#92c945 50%,#8dc63f)}
.contact .c{position:absolute;top:27px;display:flex;align-items:center;gap:10px;color:var(--white)}
.contact .ring{width:51px;height:51px;border-radius:50%;border:2px solid var(--white);display:flex;align-items:center;justify-content:center}
.contact b{font-family:'Roboto Condensed',sans-serif;font-size:13px;display:block}
.contact small{font-size:7px;font-weight:700;text-transform:uppercase}
.dark{top:814px;left:0;width:860px;height:347px;background:var(--dark);color:var(--white)}
.h-cap{font-family:'Roboto Condensed',sans-serif;font-weight:700;font-size:17px}
.h-cap .cap{font-size:40px;color:var(--teal);line-height:30px}
.h-cap .cap.g{color:var(--green)}
.connect{position:absolute;top:34px;left:0;width:860px;text-align:center}
.social{position:absolute;top:76px;left:386px;display:flex;gap:5px}
.social span{width:26px;height:26px;border:1px solid #ddd;border-radius:2px}
.fcol{position:absolute;top:135px}
.fcol .uline{width:16px;height:2px;background:var(--white);margin:2px 0 0}
.email{margin-top:17px;width:175px;height:32px;border-radius:16px;background:#c9c9c9;font-size:7px;color:#666;padding:12px 16px}
.sub{margin:4px 0 0 5px;width:92px;height:23px;border-radius:12px;background:var(--teal);font-size:9px;font-family:'Roboto Condensed',sans-serif;font-weight:700;display:flex;align-items:center;justify-content:center}
.tweet{font-size:8.5px;line-height:12.5px;color:#ddd;width:180px;padding:8px 0;border-bottom:1px solid #444}
.tweet:first-of-type{margin-top:8px}
.tweet a{color:var(--teal)}
.map{margin-top:17px;width:194px;height:106px;background:linear-gradient(135deg,#e6e3dc 0%,#dcd9d1 55%,#9fb9dc 75%,#8fb0d9 100%)}
.footer{top:1161px;left:0;width:860px;height:39px;background:var(--teal);color:var(--white);font-size:7px}
.footer nav{position:absolute;left:112px;top:16px;display:flex;gap:25px}
.footer .copy{position:absolute;right:115px;top:16px}
</style>
</head>
<body>
<div class="abs topbar">
  <div class="item" style="left:116px"><span class="ico"></span>Adress : 48 Harbor Lane, NY</div>
  <div class="item" style="left:286px"><span class="ico"></span>Email : info@veldora.com</div>
  <div class="item" style="left:441px"><span class="ico"></span>Call us : 555-010-2468</div>
  <div class="item" style="left:566px"><span class="ico" style="border-radius:50%"></span>My account</div>
  <div class="btn-sm" style="left:637px;width:46px;background:var(--teal)">LOGIN</div>
  <div class="btn-sm" style="left:685px;width:58px;background:var(--green)">REGISTER</div>
</div>

<header class="abs header">
  <div class="brand"><span class="mark"></span><span class="name">VELDORA</span></div>
  <div class="cart">
    <div class="box"><svg width="24" height="20" viewBox="0 0 24 20" fill="none" stroke="#fff" stroke-width="1.6"><path d="M1 2h4l3 11h12l2-8H6"/><circle cx="10" cy="17" r="1.5"/><circle cx="18" cy="17" r="1.5"/></svg></div>
    <div><div class="t1">SHOPPING CART</div><div class="t2"><b>(0)</b>ITEM SELECTED</div></div>
  </div>
  <div class="search">Search Product...<span class="go"><svg width="16" height="16" viewBox="0 0 16 16" fill="none" stroke="#fff" stroke-width="1.5"><circle cx="7.5" cy="7.5" r="3"/><path d="M10 10l2 2"/></svg></span></div>
</header>

<nav class="abs nav"><a>HOME</a><a>ABOUT US</a><a>HOW IT WORKS</a><a>OUR PLATFORM</a><a>BENEFITS</a><a>CONTACT US</a></nav>

<div class="abs hero" role="img" aria-label="Close-up photo of a smiling young woman in glasses by a brick wall"></div>

<h1 class="abs title"><span class="rule short"></span><span class="cap">W</span>HITE PAPER<span class="rule"></span></h1>
<p class="abs intro">Ut sit amet pretium ipsum. Mauris feugiat interdum maximus. Suspendisse ac vulputate odio. Sed id varius est, quis efficitur lorem. Mauris vel ligula interdum, gravida neque eu, consectetur nulla. Donec maximus rutrum lorem vel blandit. Suspendisse malesuada feugiat lorem. Ut sit amet pretium ipsum. Mauris feugiat interdum maximus. Suspendisse ac vulputate odio. Sed id varius est, quis efficitur lorem. Mauris vel ligula interdum, gravida neque....</p>

<section class="abs col" style="left:115px">
  <h3>TEMPOR FELIS LOREM</h3>
  <p>Ut sit amet pretium ipsum. Mauris feugiat interdum maximus. Suspendisse ac vulputate odio. Sed id varius est, quis efficitur lorem. Mauris vel ligula interdum, gravida neque eu, consectetur nulla.</p>
  <p>Donec maximus rutrum lorem vel blandit. Suspendisse malesuada feugiat lorem. Ut sit amet pretium ipsum. Mauris feugiat interdum maximus. Suspendisse ac vulputate odio. Sed id varius est, quis efficitur lorem. Mauris vel ligula interdum, gravida neque....</p>
  <span class="btn">READ MORE</span>
</section>
<div class="abs divider"></div>
<section class="abs col" style="left:454px">
  <h3>TEMPOR FELIS LOREM</h3>
  <p>Ut sit amet pretium ipsum. Mauris feugiat interdum maximus. Suspendisse ac vulputate odio. Sed id varius est, quis efficitur lorem. Mauris vel ligula interdum, gravida neque eu, consectetur nulla.</p>
  <p>Donec maximus rutrum lorem vel blandit. Suspendisse malesuada feugiat lorem. Ut sit amet pretium ipsum. Mauris feugiat interdum maximus. Suspendisse ac vulputate odio. Sed id varius est, quis efficitur lorem. Mauris vel ligula interdum, gravida neque....</p>
  <span class="btn">READ MORE</span>
</section>

<section class="abs contact" role="img" aria-label="Contact band over a faint photo of smiling people">
  <div class="c" style="left:123px"><span class="ring"><svg width="22" height="22" viewBox="0 0 24 24" fill="#fff"><path d="M6.6 10.8a15 15 0 006.6 6.6l2.2-2.2c.3-.3.7-.4 1-.2 1.1.4 2.3.6 3.6.6.6 0 1 .4 1 1V20c0 .6-.4 1-1 1A17 17 0 013 4c0-.6.4-1 1-1h3.5c.6 0 1 .4 1 1 0 1.3.2 2.5.6 3.6.1.3 0 .7-.2 1z"/></svg></span><div><b>555-010-2468</b><small>Call us for enquiry</small></div></div>
  <div class="c" style="left:335px"><span class="ring"><svg width="22" height="18" viewBox="0 0 22 18" fill="none" stroke="#fff" stroke-width="1.5"><rect x="1" y="1" width="20" height="16"/><path d="M1 1l10 9 10-9M1 17l7-7M21 17l-7-7"/></svg></span><div><b>info@veldora.com</b><small>Drop us a line anytime!</small></div></div>
  <div class="c" style="left:569px"><span class="ring"><svg width="18" height="24" viewBox="0 0 18 24" fill="#fff"><path d="M9 0a9 9 0 00-9 9c0 7 9 15 9 15s9-8 9-15a9 9 0 00-9-9zm0 12a3 3 0 110-6 3 3 0 010 6z"/></svg></span><div><b>48 Harbor Lane, NY</b><small>Company address</small></div></div>
</section>

<section class="abs dark">
  <h2 class="connect h-cap"><span class="cap">C</span>ONNECT WITH US</h2>
  <div class="social"><span aria-label="Social link"></span><span aria-label="Social link"></span><span aria-label="Social link"></span></div>

  <div class="fcol" style="left:115px">
    <h2 class="h-cap"><span class="cap">N</span>EWSLETTER</h2><div class="uline"></div>
    <div class="email">ENTER YOUR EMAIL ID</div>
    <div class="sub">SUBSCRIBE</div>
  </div>
  <div class="fcol" style="left:333px">
    <h2 class="h-cap"><span class="cap">U</span>PDATES</h2><div class="uline"></div>
    <p class="tweet"><a>@veldora_hq:</a> Phasellus dapibus tellus at nibh lobortis, vitae placerat sapien tempor.</p>
    <p class="tweet"><a>@veldora_hq:</a> Phasellus dapibus tellus at nibh lobortis, vitae placerat sapien tempor.</p>
    <p class="tweet" style="border:0"><a>@veldora_hq:</a> Phasellus dapibus tellus at nibh lobortis, vitae placerat sapien tempor.</p>
  </div>
  <div class="fcol" style="left:542px">
    <h2 class="h-cap"><span class="cap g">L</span>OCATION</h2><div class="uline"></div>
    <div class="map" role="img" aria-label="Street map showing the company location near the coast"></div>
  </div>
</section>

<footer class="abs footer">
  <nav><span>HOME</span><span>ABOUT US</span><span>HOW IT WORKS</span><span>OUR PLATFORM</span><span>BENEFITS</span><span>CONTACT US</span></nav>
  <div class="copy">© 2018 VELDORA . ALL RIGHTS RESERVED</div>
</footer>
</body>
</html>
```